"Recently Leased" flyer for real estate agency

Looking to have a Recently Leased flyer designed. This will be delivered to apartments and houses closely situated to a property we have recently leased. The idea is to get the attention of owner/landlords in the area that may be considering leasing their property in the future and inform them of the great work we are doing locally. I would like the design to be a two sided flyer using the photoshop (PSD) template below (we would like to be able to edit this once complete should we need to update copy etc in the future). I would like the front page to look like our "for lease sign with the leased sticker on it and copy, I dont want it to look like a typical junk mail flyer.

Target Market(s)

Property owners and investors, male and female aged 28-70

Industry/Entity Type

Real Estate

Font styles to use
Sans Serif

Colors

Designer to choose colors to be used in the design.

Requirements
Must have
• Harbor Keystone Logo
• Contact information
• Copy supplied
Nice to have
• Slick, clean design,
Should not have
• too many colours or too busy a design.
• NO PROPERTY PHOTOS ON FRONT - I want this to be generic and not relate to a specific property image which might confuse people.

```html
<!DOCTYPE html>
<html lang="en">
<head>
<meta charset="utf-8">
<title>Harbor Keystone – Recently Leased Flyer</title>
<link href="https://fonts.googleapis.com/css2?family=Montserrat:wght@800&family=Open+Sans:wght@300;400;600&family=Oswald:wght@500&display=swap" rel="stylesheet">
<style>
:root{
  --bg:#e8ebec;
  --paper:#ffffff;
  --teal:#3dbb95;
  --teal-dark:#2f8f7c;
  --mint:#c8eee2;
  --ink:#2a2d2e;
  --text:#3c4142;
  --charcoal:#3a4040;
  --name:#4a8fd8;
  --bullet:#1f55c8;
  --sky-top:#2f4fd6;
  --sky-low:#8fc3f0;
}
*{box-sizing:border-box;margin:0;padding:0}
html,body{width:1200px;height:1200px;overflow:hidden}
body{background:var(--bg);font-family:"Open Sans",Arial,sans-serif;color:var(--text)}
.flyer{position:absolute;top:95px;width:480px;height:1010px;background:var(--paper);overflow:hidden;box-shadow:0 6px 22px rgba(0,0,0,.12)}
.flyer--front{left:70px}
.flyer--back{left:650px}
.art{position:absolute;left:0;top:0;display:block}
.brand{position:absolute;display:flex;align-items:center;gap:10px;font-family:"Montserrat",Arial,sans-serif;font-weight:800;color:var(--ink);letter-spacing:.5px;white-space:nowrap}
.brand__mark{width:14px;height:14px;background:var(--teal)}
.flyer--front .brand{left:50px;top:400px;font-size:31px}
.flyer--back .brand{right:26px;top:38px;font-size:21px}
.copy{position:absolute;left:44px;right:40px;font-size:12.6px;line-height:1.42}
.copy p{margin-bottom:14px}
.copy ul{list-style:none;margin-bottom:16px}
.copy li{position:relative;padding-left:18px;margin-bottom:1px}
.copy li::before{content:"";position:absolute;left:2px;top:7px;width:6px;height:6px;border-radius:50%;background:var(--bullet)}
.flyer--front .copy{top:470px}
.flyer--back .copy{top:225px}
.contact{position:absolute;display:flex;align-items:flex-end;gap:26px}
.agent__name{font-weight:300;font-size:31px;color:var(--name);line-height:1}
.agent__firm{font-size:11.5px;color:var(--name)}
.phone{display:flex;align-items:center;gap:6px;font-family:"Oswald",Arial,sans-serif;font-weight:500;font-size:27px;color:var(--teal);line-height:1}
.address{font-size:11.5px;line-height:1.35;color:var(--text);margin-top:6px}
.flyer--front .contact{left:44px;top:788px}
.flyer--back .contact{left:40px;top:620px}
.web{position:absolute;font-size:12px;line-height:1.7}
.web div{display:flex;align-items:center;gap:8px}
.flyer--front .web{left:60px;bottom:36px;color:#fff}
.flyer--back .web{left:200px;bottom:38px;color:var(--ink)}
.photo{position:absolute}
.photo--left{left:0;top:780px;width:170px;height:230px;background:linear-gradient(160deg,#1e2fa8,#5b7ee6 55%,#c9b6e8)}
.photo--right{left:170px;top:700px;width:310px;height:190px;background:linear-gradient(170deg,#2c5db8,#7fb0e6 50%,#b7b08e 85%)}
.band-mint{position:absolute;left:170px;top:890px;width:310px;height:120px;background:var(--mint)}
</style>
</head>
<body>

<section class="flyer flyer--front">
  <svg class="art" width="480" height="1010" viewBox="0 0 480 1010">
    <defs>
      <linearGradient id="sky" x1="0" y1="0" x2="0" y2="1">
        <stop offset="0" stop-color="#2f4fd6"/>
        <stop offset=".7" stop-color="#8fc3f0"/>
        <stop offset="1" stop-color="#3b4a6a"/>
      </linearGradient>
    </defs>
    <g role="img" aria-label="Photo of a modern apartment building at dusk">
      <polygon points="0,0 480,0 480,180 300,300 0,300" fill="url(#sky)"/>
    </g>
    <polygon points="480,120 480,300 300,300" fill="var(--teal)" opacity=".92"/>
    <polygon points="0,310 260,310 0,440" fill="var(--teal)" opacity=".92"/>
    <polygon points="0,960 480,860 480,1010 0,1010" fill="var(--charcoal)"/>
    <polygon points="0,900 480,800 480,860 0,960" fill="#fff"/>
  </svg>

  <div class="brand"><span class="brand__mark"></span>HARBOR KEYSTONE</div>

  <div class="copy">
    <p>We recently leased a property in your building or street. Attracting a great reliable tenant and fantastic return for the owner. We received a high number of enquires and applications for this property and have a database of screened and qualified tenants looking to lease in your area.</p>
    <ul>
      <li>On average we lease properties 2 weeks faster than the Seaview average</li>
      <li>Strong database of tenants actively looking in the area</li>
      <li>All we do is lease property, no sales – so tenanting and managing your property is our priority</li>
      <li>90 day money back guarantee on our level of service</li>
      <li>Highly competitive, simple all-inclusive pricing</li>
      <li>Experience the difference of a property management specialist</li>
    </ul>
    <p>Contact Sam to get your free rental appraisal or transfer your existing investment to an agency that will give it the attention it deserves and maximise your return.</p>
  </div>

  <div class="contact">
    <div class="agent">
      <div class="agent__name">Sam Ridley</div>
      <div class="agent__firm">Harbor Keystone Agency</div>
    </div>
    <div>
      <div class="phone">
        <svg width="20" height="20" viewBox="0 0 24 24" fill="none" stroke="#555" stroke-width="1.6"><circle cx="12" cy="12" r="10"/><path d="M8 7l2 2-1 2c1 2 2 3 4 4l2-1 2 2-2 2c-4 0-9-5-9-9z"/></svg>
        0400 555 218
      </div>
      <div class="address">Level 1, 12 Cove Rd, Seaview<br>NSW 2000</div>
    </div>
  </div>

  <div class="web">
    <div><svg width="16" height="12" viewBox="0 0 16 12" fill="none" stroke="#fff" stroke-width="1.2"><rect x=".6" y=".6" width="14.8" height="10.8"/><path d="M.6.6 8 7l7.4-6.4"/></svg>sam@harborkeystone.com.au</div>
    <div><svg width="16" height="16" viewBox="0 0 16 16" fill="none" stroke="#fff" stroke-width="1.2"><circle cx="8" cy="8" r="7"/><path d="M1 8h14M8 1c3 3 3 11 0 14M8 1c-3 3-3 11 0 14"/></svg>www.harborkeystone.com.au</div>
  </div>
</section>

<section class="flyer flyer--back">
  <svg class="art" width="480" height="200" viewBox="0 0 480 200">
    <polygon points="170,0 480,0 480,95 100,95" fill="var(--mint)"/>
    <polygon points="0,105 190,105 150,170" fill="var(--teal)"/>
    <polygon points="165,105 195,105 150,170 140,155" fill="var(--teal-dark)"/>
    <polygon points="0,95 480,95 480,110 0,110" fill="var(--teal)"/>
    <polygon points="160,140 480,100 480,112 155,152" fill="var(--teal)" opacity=".9"/>
    <rect x="0" y="172" width="480" height="18" fill="var(--teal)"/>
  </svg>

  <div class="brand"><span class="brand__mark"></span>HARBOR KEYSTONE</div>

  <div class="copy">
    <p>The fundamental idea behind Harbor Keystone Agency was to give landlords a simple and confidence inspiring experience. We achieve this through:</p>
    <ul>
      <li>Unique marketing that goes beyond the standard listing sites and has seen our average days-on-market at 5.9days for 2018.</li>
      <li>A simple, yet competitive fee structure.</li>
      <li>Excellent customer service through an experienced professional property manager.</li>
      <li>Sound advice and communication through out the leasing and management process.</li>
      <li>A simple yet powerful landlord portal which enables owners to view media rich inspection reports, financial reports and maintenance progress at anytime.</li>
      <li>We then back our service promise with a 90day money back guarantee.</li>
    </ul>
    <p>If you have been considering leasing your property, purchasing a local investment or aren't happy with your current managing agency, please don't hesitate to contact your local rental specialist for more information:</p>
  </div>

  <div class="contact">
    <div class="agent">
      <div class="agent__name">Sam Ridley</div>
      <div class="agent__firm">Harbor Keystone Agency</div>
    </div>
    <div>
      <div class="phone">
        <svg width="20" height="20" viewBox="0 0 24 24" fill="none" stroke="#555" stroke-width="1.6"><circle cx="12" cy="12" r="10"/><path d="M8 7l2 2-1 2c1 2 2 3 4 4l2-1 2 2-2 2c-4 0-9-5-9-9z"/></svg>
        0400 555 218
      </div>
      <div class="address">Level 1, 12 Cove Rd, Seaview<br>NSW 2000</div>
    </div>
  </div>

  <div class="photo photo--left" role="img" aria-label="Photo of a lit apartment tower at dusk"></div>
  <div class="photo photo--right" role="img" aria-label="Photo of a modern apartment block with timber balconies"></div>
  <div class="band-mint"></div>

  <div class="web">
    <div><svg width="16" height="12" viewBox="0 0 16 12" fill="none" stroke="#2a2d2e" stroke-width="1.2"><rect x=".6" y=".6" width="14.8" height="10.8"/><path d="M.6.6 8 7l7.4-6.4"/></svg>sam@harborkeystone.com.au</div>
    <div><svg width="16" height="16" viewBox="0 0 16 16" fill="none" stroke="#2a2d2e" stroke-width="1.2"><circle cx="8" cy="8" r="7"/><path d="M1 8h14M8 1c3 3 3 11 0 14M8 1c-3 3-3 11 0 14"/></svg>www.harborkeystone.com.au</div>
  </div>
</section>

</body>
</html>
```